Wordpress Design Project For Budget Hotel

Although it is a budget hotel we would like a mid to upmarket word press web design with relatively prominent images of local attractions. The design needs to be clean and professional looking.

This is design only. The design/files most be easy for our developer to work with and develop the back end/code.

The website will contain 6 pages:
Homepage
Accommodation & Rates
Facilities
Attractions
Bookings
Contact us

The full content is provided in a word doc which i have uploaded along with all the images needed.

Target Market(s)

The target audience are budget travelers looking for clean and comfortable accommodation at an affordable price.

Industry/Entity Type

Hotel

Requirements
Must have
• Prominent images of local attractions in a changing background or as a sliding banner.

Roomly Hotel Reservation booking form. A small one on the home page and full one on the booking page.

Google maps window in the contact page
Should not have
• We dont want to many bright colours (ie yellow, red) but clean white is fine

```html
<!DOCTYPE html>
<html lang="en">
<head>
<meta charset="utf-8">
<title>Ridgeline Hotel Bellmore – Bookings</title>
<link rel="stylesheet" href="https://fonts.googleapis.com/css2?family=Arimo:wght@400;700&family=Gelasio:ital@0;1&display=swap">
<style>
:root{
  --brand-blue:#3d9fe4;
  --leaf-green:#7dc843;
  --nav-grey:#9a9a9a;
  --ink:#2e2e2e;
  --soft-ink:#555;
  --frame:#555;
  --rule:#666;
  --field-border:#333;
  --page:#ffffff;
}
*{box-sizing:border-box;margin:0;padding:0}
html,body{width:1200px;height:960px;overflow:hidden;background:var(--page)}
body{position:relative;font-family:"Arimo",Arial,sans-serif;color:var(--ink)}
.abs{position:absolute}

.site-name{left:24px;top:30px;font-size:38px;font-weight:400;color:var(--brand-blue);line-height:1}
.top-contact{right:12px;top:46px;display:flex;align-items:center;gap:8px;font-family:"Gelasio",serif;font-size:15px;color:var(--ink)}
.top-contact .divider{width:1px;height:20px;background:#ccc}

.main-nav{left:24px;top:89px;display:flex;gap:30px;font-size:16px;text-transform:uppercase;color:var(--nav-grey);letter-spacing:0.3px}
.main-nav .current{color:var(--ink)}

.page-title{left:384px;top:132px;font-size:20px;font-weight:700;color:var(--ink)}
.contact-list{left:406px;top:183px;font-family:"Gelasio",serif;font-size:16px;line-height:20px;color:#111}
.contact-list .row{display:flex}
.contact-list .label{width:86px}
.contact-list .colon{width:43px}
.contact-list .link{text-decoration:underline}

.booking-heading{left:410px;top:319px;font-size:18px;font-weight:400;color:var(--ink)}
.panel{border:1px solid var(--frame);border-radius:6px;background:var(--page)}
.language-bar{left:409px;top:350px;width:675px;height:38px;display:flex;align-items:center;gap:5px;padding-left:10px}
.language-bar span{width:21px;height:14px;border:1px solid #bbb;border-radius:2px}
.search-panel{left:409px;top:395px;width:675px;height:255px;font-family:"Gelasio",serif;color:var(--soft-ink)}
.help{right:34px;top:14px;font-style:italic;font-size:15px;display:flex;align-items:center;gap:7px}
.field-label{font-size:14px;letter-spacing:0.8px}
.date-field{width:103px;height:26px;border:1px solid var(--field-border);font-size:14px;padding:3px 6px;letter-spacing:1px}
.divider-line{left:26px;width:608px;height:1px;background:var(--rule)}
.persons-select{left:216px;top:114px;width:52px;height:23px;border:1px solid #4a7ba8;font-size:12px;padding:5px 8px;color:#111}
.persons-select .arrow{position:absolute;right:0;top:0;width:18px;height:21px;background:#cfe4f5;display:flex;align-items:center;justify-content:center}
.search-button{left:537px;top:184px;width:90px;height:27px;border:1px solid #888;border-radius:3px;background:linear-gradient(#fafafa,#d8d8d8);font-family:"Gelasio",serif;font-size:17px;color:#111;display:flex;align-items:center;justify-content:center}
.calendar-link{left:409px;top:658px;width:675px;height:42px;font-family:"Gelasio",serif;font-size:14px;color:var(--soft-ink);padding:11px 14px;letter-spacing:0.4px}
.powered{left:716px;top:709px;font-family:"Gelasio",serif;font-size:11px;color:var(--soft-ink)}
.powered u{text-decoration:underline}

.footer-mark{left:40px;top:840px;width:50px;height:50px;background:var(--leaf-green)}
.footer-address{left:122px;top:856px;font-size:16px;line-height:24px;color:#444}
</style>
</head>
<body>

<header>
  <div class="abs site-name">Ridgeline Hotel Bellmore</div>
  <div class="abs top-contact">
    <svg width="30" height="20" viewBox="0 0 30 20" aria-hidden="true"><rect x="1.5" y="1.5" width="27" height="17" fill="none" stroke="var(--leaf-green)" stroke-width="3"/><path d="M2 2 L15 12 L28 2" fill="none" stroke="var(--leaf-green)" stroke-width="3"/></svg>
    <span class="divider"></span>
    <svg width="20" height="20" viewBox="0 0 24 24" aria-hidden="true"><path fill="var(--leaf-green)" d="M6.6 10.8a15.1 15.1 0 0 0 6.6 6.6l2.2-2.2c.3-.3.7-.4 1-.2 1.1.4 2.3.6 3.6.6.6 0 1 .4 1 1V20c0 .6-.4 1-1 1A17 17 0 0 1 3 4c0-.6.4-1 1-1h3.5c.6 0 1 .4 1 1 0 1.3.2 2.5.6 3.6.1.3 0 .7-.2 1z"/></svg>
    <span>02 5550 1847</span>
  </div>
  <nav class="abs main-nav">
    <span>Home</span><span>Accomodations</span><span>Facilities</span><span>Attractions</span><span class="current">Bookings</span><span>Contact</span>
  </nav>
</header>

<main>
  <h1 class="abs page-title">BOOK ROOM</h1>
  <div class="abs contact-list">
    <div class="row"><span class="label">Phone</span><span class="colon">:</span><span>02 5550 1847</span></div>
    <div class="row"><span class="label">Address</span><span class="colon">:</span><span>14-18 Wattle St, BELLMORE, NSW 2499</span></div>
    <div class="row"><span class="label">Email</span><span class="colon">:</span><span class="link">stay@ridgelinehotelbellmore.example</span></div>
  </div>

  <h2 class="abs booking-heading">ONLINE BOOKING</h2>

  <div class="abs panel language-bar" role="img" aria-label="Language selection flags">
    <span style="background:#3a4fa0"></span><span style="background:#e8e8f4"></span><span style="background:#b33"></span><span style="background:#e8b020"></span><span style="background:#3a9a40"></span><span style="background:#c04040"></span><span style="background:#c04a3a"></span><span style="background:#3a9a40"></span><span style="background:#e0c020"></span><span style="background:#d8c030"></span><span style="background:#e8eef8"></span><span style="background:#cc3030"></span><span style="background:#c03040"></span><span style="background:#2a5a9a"></span>
  </div>

  <section class="abs panel search-panel">
    <div class="abs help">Help
      <svg width="20" height="20" viewBox="0 0 20 20" aria-hidden="true"><circle cx="10" cy="10" r="9" fill="#eef4fb" stroke="#4a7ba8" stroke-width="1.4"/><text x="10" y="15" text-anchor="middle" font-size="13" font-family="Arimo, sans-serif" fill="#4a7ba8">?</text></svg>
    </div>

    <div class="abs field-label" style="left:59px;top:36px">Check-in:</div>
    <div class="abs date-field" style="left:58px;top:57px">08/31/2013</div>
    <svg class="abs" style="left:166px;top:60px" width="18" height="20" viewBox="0 0 18 20" aria-hidden="true"><rect x="0.5" y="2.5" width="17" height="17" fill="#fff" stroke="#5a8ac0"/><rect x="0.5" y="2.5" width="17" height="4" fill="#5a8ac0"/><g fill="#8aa"><rect x="3" y="9" width="2" height="2"/><rect x="7" y="9" width="2" height="2"/><rect x="11" y="9" width="2" height="2"/><rect x="3" y="13" width="2" height="2"/><rect x="7" y="13" width="2" height="2"/><rect x="11" y="13" width="2" height="2"/></g></svg>

    <div class="abs field-label" style="left:211px;top:38px">Check-out</div>
    <div class="abs date-field" style="left:210px;top:57px">09/31/2013</div>
    <svg class="abs" style="left:318px;top:60px" width="18" height="20" viewBox="0 0 18 20" aria-hidden="true"><rect x="0.5" y="2.5" width="17" height="17" fill="#fff" stroke="#5a8ac0"/><rect x="0.5" y="2.5" width="17" height="4" fill="#5a8ac0"/><g fill="#8aa"><rect x="3" y="9" width="2" height="2"/><rect x="7" y="9" width="2" height="2"/><rect x="11" y="9" width="2" height="2"/><rect x="3" y="13" width="2" height="2"/><rect x="7" y="13" width="2" height="2"/><rect x="11" y="13" width="2" height="2"/></g></svg>
    <div class="abs field-label" style="left:360px;top:64px">Nights: 1</div>

    <div class="abs divider-line" style="top:99px"></div>

    <div class="abs field-label" style="left:64px;top:117px">Number of Persons</div>
    <div class="abs persons-select">1<span class="arrow"><svg width="10" height="6" viewBox="0 0 10 6" aria-hidden="true"><path d="M0 0 H10 L5 6Z" fill="#234"/></svg></span></div>

    <div class="abs divider-line" style="top:153px"></div>

    <div class="abs search-button">Search »</div>
  </section>

  <div class="abs panel calendar-link">Show availability in calendar overview &gt;&gt;</div>
  <div class="abs powered">Powered by <u>Roomly</u>™ <u>Hotel Booking System</u> Copyright © 2008-2013</div>
</main>

<footer>
  <div class="abs footer-mark" aria-hidden="true"></div>
  <div class="abs footer-address">
    <div>14-18 Wattle St</div>
    <div>BELLMORE, NSW 2499</div>
    <div>ABN 00111222333</div>
  </div>
</footer>

</body>
</html>
```